依頼詳細
福利厚生用の封筒デザインを依頼します。利用用途は、お誕生日の際お贈りするプレゼント(商品券)をお渡しする際使わせていただきます。デザインは「福利厚生」とはいえおめでたい事で「常日頃の感謝を形」にしたいので、見るだけでHAPPYになるような遊び心のある封筒を希望いたします。又男女共に使用できるデザインにしていただけると幸いです。
記載項目
■「お誕生日おめでとうございます」「HAPPY BIRTHDAY」等、お誕生日関係だとわかるようなもの。
■会社名:tavenorgroup(テキストとロゴをお願いいたします)
サイズ
設定なし
希望イメージ
シンプル 複雑
単色 カラフル
暗い 明るい
日常 高級
遊び心 厳粛
未来的 伝統的
女性的 男性的
希望する色
特にこだわりはございません。
納品ファイル
• 高解像度JPG (.jpg)
• イラストレーター形式 (.ai)
補足説明
法人ですが、厳粛なイメージではなく遊び心のあるものを楽しみにお待ちしております!
依頼公開後の追記内容
大変急ではございますが、サイズが洋長3となりました。
恐れ入りますが今後ご提案くださる予定のデザイナーの方々は
洋長3でレイアウトしていただけますようお願い申し上げます。
■ 選んだ理由

シンプルながら紅白のコントラストが魅力的で
成人男女・お子さん等 どなたにも
喜んでいただけるデザインだと感じました。

■ 提案者全員のお礼・コメント

ご提案いただきました全てのミルダー様

この度はご多忙中素敵なご提案を頂きまして誠に有難う御座いました。
どの作品も個々特徴的で、作品を拝見するのが楽しみな日々でした。

今後も何処かのタイミングでquintaroを使わせていただくかと思いますので
御縁がございましたら次回もどうぞ宜しくお願い申し上げます。

tavenorgroup広報担当

```html
<!DOCTYPE html>
<html lang="ja">
<head>
<meta charset="utf-8">
<title>Tavenor Group Birthday Envelope</title>
<link rel="stylesheet" href="https://fonts.googleapis.com/css2?family=Fredoka:wght@600&family=Nunito:wght@800&display=swap">
<style>
  :root {
    --paper: #ffffff;
    --dieline: #b9bcc0;
    --crop: #6f7276;
    --ribbon: #8fc9ea;
    --bow-red: #e8442d;
    --bow-yellow: #f4c51c;
    --label-blue: #2b6cb0;
    --sky-top: #e3f4fc;
    --sky-bottom: #c4e6f7;
    --grass-light: #a6d98a;
    --grass: #7cc36a;
    --sun: #e8442d;
    --text-red: #e64a2e;
  }
  html, body {
    margin: 0;
    padding: 0;
    overflow: hidden;
    background: var(--paper);
  }
  .sheet { width: 900px; height: 1200px; display: block; }
  .dieline { fill: none; stroke: var(--dieline); stroke-width: 2; }
  .crop-mark { stroke: var(--crop); stroke-width: 1; }
  .ribbon { fill: var(--ribbon); }
  .company-name {
    font-family: "Nunito", sans-serif;
    font-weight: 800;
    fill: var(--label-blue);
  }
  .greeting {
    font-family: "Fredoka", sans-serif;
    font-weight: 600;
    font-size: 38px;
    letter-spacing: 1px;
    fill: var(--text-red);
  }
</style>
</head>
<body>
<svg class="sheet" viewBox="0 0 900 1200" xmlns="http://www.w3.org/2000/svg">
  <defs>
    <linearGradient id="scene-fill" x1="0" y1="0" x2="0" y2="1">
      <stop offset="0" stop-color="var(--sky-top)"/>
      <stop offset="0.5" stop-color="var(--sky-bottom)"/>
      <stop offset="0.58" stop-color="var(--grass-light)"/>
      <stop offset="1" stop-color="var(--grass)"/>
    </linearGradient>
    <path id="greeting-arc" d="M250 440 Q460 530 670 440"/>
  </defs>

  <!-- Front of envelope -->
  <g class="envelope-front">
    <rect class="dieline" x="66" y="45" width="780" height="519"/>
    <path class="dieline" d="M66 45 L96 100 Q111 115 141 115 L771 115 Q801 115 816 100 L846 45"/>
    <rect class="ribbon" x="435" y="45" width="51" height="519"/>
    <rect class="ribbon" x="66" y="336" width="780" height="30"/>

    <rect role="img" aria-label="Red gift bow on the ribbon" x="240" y="318" width="60" height="72" rx="10" fill="var(--bow-red)"/>
    <rect role="img" aria-label="Yellow gift bow on the ribbon" x="585" y="318" width="60" height="72" rx="10" fill="var(--bow-yellow)"/>

    <g class="company-label">
      <rect x="370" y="245" width="172" height="150" rx="10" fill="var(--paper)"/>
      <rect x="432" y="258" width="56" height="56" fill="var(--label-blue)"/>
      <text class="company-name" x="460" y="356" font-size="28" text-anchor="middle">Tavenor Group</text>
    </g>

    <text class="greeting"><textPath href="#greeting-arc" startOffset="50%" text-anchor="middle">HAPPY BIRTHDAY</textPath></text>
  </g>

  <!-- Back of envelope -->
  <g class="envelope-back">
    <rect class="dieline" x="66" y="720" width="780" height="450"/>
    <path class="dieline" d="M66 720 L96 775 Q111 790 141 790 L771 790 Q801 790 816 775 L846 720"/>
    <rect role="img" aria-label="Birthday scene: sky with clouds, a row of trees, a small yellow car, a flag and a cake-shaped house with candles on green grass" x="66" y="900" width="780" height="270" fill="url(#scene-fill)"/>
    <circle cx="765" cy="891" r="21" fill="var(--sun)"/>
    <rect class="ribbon" x="435" y="720" width="51" height="450"/>
    <rect class="ribbon" x="66" y="954" width="780" height="36"/>

    <g class="company-label">
      <rect x="318" y="868" width="30" height="30" fill="var(--label-blue)"/>
      <text class="company-name" x="356" y="892" font-size="25">Tavenor Group</text>
    </g>
  </g>

  <!-- Crop marks -->
  <g class="crop-marks">
    <line class="crop-mark" x1="30" y1="45" x2="56" y2="45"/>
    <line class="crop-mark" x1="66" y1="15" x2="66" y2="35"/>
    <line class="crop-mark" x1="856" y1="45" x2="882" y2="45"/>
    <line class="crop-mark" x1="846" y1="15" x2="846" y2="35"/>
    <line class="crop-mark" x1="30" y1="564" x2="56" y2="564"/>
    <line class="crop-mark" x1="856" y1="564" x2="882" y2="564"/>
    <line class="crop-mark" x1="30" y1="720" x2="56" y2="720"/>
    <line class="crop-mark" x1="856" y1="720" x2="882" y2="720"/>
    <line class="crop-mark" x1="30" y1="1170" x2="56" y2="1170"/>
    <line class="crop-mark" x1="66" y1="1178" x2="66" y2="1196"/>
    <line class="crop-mark" x1="856" y1="1170" x2="882" y2="1170"/>
    <line class="crop-mark" x1="846" y1="1178" x2="846" y2="1196"/>
  </g>
</svg>
</body>
</html>
```